Marbrook Jewelers New Website Design

This project is to provide a new design for an existing website. The existing website is marbrookjewelers dot com . I have created a overview document that outlines all the details for the project. I do not need the design to be converted into HTML. I have a team for that already so please don't ask. I have a lot of images .. too many to upload here so they are on my dev server located at pinfernstudio com slash marbrook slash assets

Number of Pages Required

1 page

```html
<!DOCTYPE html>
<html lang="en">
<head>
<meta charset="utf-8">
<title>Marbrook Jewelers</title>
<link href="https://fonts.googleapis.com/css2?family=Cormorant+Garamond:wght@300;400;500;600&family=Lato:wght@400;700&display=swap" rel="stylesheet">
<style>
:root{
  --ink:#2b2b2b;
  --muted:#6d6d6d;
  --white:#ffffff;
  --hero-bg:#efefef;
  --aqua:#bfe8ec;
  --pale-blue:#d3e5e9;
  --soft-grey:#e7e7e7;
  --navy:#121722;
  --footer:#1d1d1d;
  --gold:#b99b5f;
  --teal-link:#3c6f8a;
  --line:#d6d6d6;
}
*{margin:0;padding:0;box-sizing:border-box}
html,body{width:1200px;height:5106px;overflow:hidden;background:var(--white)}
body{font-family:"Lato",sans-serif;color:var(--ink);position:relative}
.serif{font-family:"Cormorant Garamond",serif;font-weight:400}
.ph{position:absolute}
a{color:inherit;text-decoration:none}

/* header */
.site-header{position:absolute;left:0;top:0;width:1200px;height:143px;background:var(--white)}
.brand{position:absolute;left:500px;top:44px;width:220px;text-align:center;font-family:"Cormorant Garamond",serif;font-size:24px;color:var(--ink);white-space:nowrap}
.brand-dot{display:inline-block;width:8px;height:8px;border-radius:50%;background:#5fb7c0;margin-right:8px;vertical-align:middle}
.contact-top{position:absolute;left:742px;top:62px;font-size:9px;font-weight:700;white-space:nowrap}
.contact-top svg{vertical-align:-2px;margin-right:4px}
.main-nav{position:absolute;left:0;top:105px;width:1200px;display:flex;justify-content:center;gap:20px;font-family:"Cormorant Garamond",serif;font-size:11px;font-weight:500}

/* hero */
.hero{position:absolute;left:0;top:143px;width:1200px;height:508px;background:var(--hero-bg)}
.hero .vline{position:absolute;top:0;width:1px;height:508px;background:var(--line)}
.eyebrow{position:absolute;left:155px;top:334px;font-size:9px;color:var(--muted)}
.eyebrow::before{content:"";display:inline-block;width:16px;height:1px;background:var(--muted);margin-right:6px;vertical-align:middle}
.hero-title{position:absolute;left:154px;top:355px;font-family:"Cormorant Garamond",serif;font-weight:300;font-size:43px;line-height:46px;color:#333}
.btn-outline{position:absolute;display:flex;align-items:center;justify-content:center;border:2px solid #444;font-size:8px;font-weight:700;background:var(--white);white-space:nowrap}
.btn-shadow{box-shadow:4px 4px 0 #bbb}
.hero-side{position:absolute;left:853px;top:421px;font-family:"Cormorant Garamond",serif;font-size:19px;line-height:25px;color:var(--gold)}
.hero-more{position:absolute;left:858px;top:489px;font-size:9px;color:var(--gold);border-bottom:1px solid var(--gold);padding-bottom:2px}
.hero-arrows{position:absolute;left:855px;top:555px}

/* custom */
.aqua-band{position:absolute;left:0;top:651px;width:1200px;height:587px;background:var(--aqua)}
.certified{position:absolute;left:142px;top:837px;width:240px;height:60px;transform:rotate(-90deg);font-family:"Cormorant Garamond",serif;font-size:29px;line-height:29px;color:#555;text-align:center;white-space:nowrap}
.custom h2{position:absolute;left:651px;top:753px;font-size:30px;line-height:34px;font-weight:400;font-family:"Cormorant Garamond",serif}
.custom p{position:absolute;left:651px;top:840px;width:300px;font-size:11.5px;line-height:19px;color:#555}
.text-link{position:absolute;font-size:8.5px;font-weight:700;border-bottom:1px solid var(--ink);padding-bottom:2px;white-space:nowrap}

/* split */
.split-label{position:absolute;left:236px;top:1360px;font-size:9px;color:#fff;border-bottom:1px solid #fff}
.split-title{position:absolute;left:233px;top:1380px;font-family:"Cormorant Garamond",serif;font-size:32px;line-height:38px;color:#fff}
.res-title{position:absolute;left:645px;top:1237px;font-family:"Cormorant Garamond",serif;font-size:34px;line-height:38px}

/* features */
.features h2{position:absolute;left:244px;top:1615px;font-family:"Cormorant Garamond",serif;font-size:30px;font-weight:400}
.card{position:absolute;width:229px;height:285px;border:1px solid #dedede;background:var(--white)}
.card .pic{position:absolute;left:30px;top:25px;width:169px;height:170px;border-radius:6px}
.card .name{position:absolute;left:22px;top:225px;font-size:11px;color:#444}
.card .price{position:absolute;left:22px;top:246px;font-size:9px;color:var(--teal-link)}
.browse{position:absolute;left:0;top:2295px;width:1200px;text-align:center;font-size:13px;line-height:24px;font-weight:700;color:#333}
.browse-rule{position:absolute;left:380px;top:2353px;width:440px;height:2px;background:#333}

/* heritage */
.heritage{position:absolute;left:0;top:2405px;width:1200px;height:500px;background:var(--navy)}
.heritage h2{position:absolute;left:252px;top:80px;font-family:"Cormorant Garamond",serif;font-weight:400;font-size:32px;line-height:35px;color:#fff}
.heritage h2 b{font-family:"Lato",sans-serif;font-weight:700}
.heritage .vrule{position:absolute;left:287px;top:186px;width:1px;height:240px;background:#cfcfcf}
.heritage p{position:absolute;left:335px;top:248px;width:315px;font-size:11.5px;line-height:20px;color:#d6d6d6}
.heritage .text-link{color:#fff;border-color:#fff;left:335px;top:402px}

/* showcase */
.showcase{position:absolute;left:0;top:2905px;width:1200px;height:635px;background:var(--soft-grey)}
.partner-mark{position:absolute;left:490px;top:3075px;width:240px;text-align:center;font-family:"Cormorant Garamond",serif;font-size:22px;letter-spacing:4px;color:#888}
.showcase-title{position:absolute;left:440px;top:3120px;width:320px;text-align:center;font-size:29px}
.showcase-text{position:absolute;left:490px;top:3172px;width:220px;text-align:center;font-size:11.5px;line-height:19px;color:#888}
.engrave-band{position:absolute;left:0;top:3540px;width:1200px;height:465px;background:var(--pale-blue)}
.engrave-card{position:absolute;left:415px;top:3545px;width:245px;height:200px;background:var(--white);display:flex;align-items:center;justify-content:center;text-align:center;font-family:"Cormorant Garamond",serif;font-size:30px;line-height:36px;box-shadow:0 2px 10px rgba(0,0,0,.08)}
.btn-small{position:absolute;height:28px;border:2px solid #333;display:flex;align-items:center;justify-content:center;font-size:9px;font-weight:700;background:transparent;white-space:nowrap}

/* gallery */
.gallery-card{position:absolute;left:520px;top:4125px;width:170px;height:100px;background:var(--white);text-align:center;padding-top:30px}
.gallery-card h3{font-family:"Cormorant Garamond",serif;font-size:26px;font-weight:400}
.gallery-card span{font-size:8px;border-bottom:1px solid var(--ink)}

/* gifts */
.gifts{position:absolute;left:0;top:4370px;width:1200px;height:400px;background:linear-gradient(90deg,#e9e9e9,#ececec 60%,#e6e6e6)}
.gift-title{position:absolute;left:243px;top:4508px;font-size:33px;line-height:40px;color:#555}
.btn-gold{position:absolute;left:243px;top:4665px;width:100px;height:26px;border:1px solid var(--gold);color:var(--gold);font-size:9px;display:flex;align-items:center;justify-content:center}
.pen-card{position:absolute;left:812px;top:4435px;width:173px;height:225px;background:var(--white);box-shadow:6px 6px 0 #d9d9d9}

/* footer */
.site-footer{position:absolute;left:0;top:4770px;width:1200px;height:336px;background:var(--footer);color:#e6e6e6}
.f-info{position:absolute;left:311px;top:65px;font-size:12.5px;line-height:24px}
.f-btn{position:absolute;left:311px;top:172px;width:190px;height:27px;border:1px solid #aaa;font-size:9px;display:flex;align-items:center;justify-content:center}
.f-rule{position:absolute;top:90px;width:1px;height:130px;background:#444}
.social{position:absolute;left:825px;font-size:10px;display:flex;align-items:center;gap:14px}
.social i{display:block;width:28px;height:28px;border-radius:50%;background:#fff}
.copyright{position:absolute;left:0;top:280px;width:1200px;text-align:center;font-size:9px;color:#bdbdbd}
</style>
</head>
<body>

<header class="site-header">
  <div class="brand"><span class="brand-dot"></span>Marbrook Jewelers</div>
  <div class="contact-top">
    <svg width="10" height="10" viewBox="0 0 24 24"><path fill="#2b2b2b" d="M6.6 10.8a15 15 0 0 0 6.6 6.6l2.2-2.2a1 1 0 0 1 1-.25 11.4 11.4 0 0 0 3.6.6 1 1 0 0 1 1 1V20a1 1 0 0 1-1 1A17 17 0 0 1 3 4a1 1 0 0 1 1-1h3.5a1 1 0 0 1 1 1c0 1.25.2 2.45.6 3.6a1 1 0 0 1-.25 1z"/></svg>Phone - 555-214-7730 &nbsp;|&nbsp; Toll Free - 888-555-0192
  </div>
  <nav class="main-nav">
    <a>Company</a><a>Custom Jewelry Services</a><a>Jewelry Repair Services</a><a>Resources</a><a>Showcase</a><a>Gallery</a><a>Engraving &amp; Trophies</a><a>Gift Ideas</a>
  </nav>
</header>

<section class="hero">
  <div class="vline" style="left:412px"></div>
  <div class="vline" style="left:823px"></div>
  <div class="ph" role="img" aria-label="Gold diamond eternity band photograph" style="left:385px;top:70px;width:450px;height:380px;background:radial-gradient(ellipse at 50% 50%,#e3cf8f 0%,#d8c380 25%,rgba(239,239,239,0) 65%)"></div>
  <div class="ph" role="img" aria-label="Green leaves decoration" style="left:1075px;top:385px;width:125px;height:140px;border-radius:50% 10% 50% 10%;background:linear-gradient(135deg,#9fbf7c,#5f8a49)"></div>
</section>
<div class="eyebrow">Marbrook Jewelers</div>
<h1 class="hero-title">Exclusive<br>jewellery collections</h1>
<a class="btn-outline btn-shadow" style="left:157px;top:479px;width:142px;height:34px">Contact Marbrook Jewelers</a>
<div class="hero-side">Diamond Wedding<br>Ring Collections</div>
<a class="hero-more">View more</a>
<svg class="hero-arrows" width="72" height="26" viewBox="0 0 72 26"><path d="M2 13h24M2 13l7-6M2 13l7 6M38 4 32 22M46 13h24M70 13l-7-6M70 13l-7 6" stroke="#333" stroke-width="1.5" fill="none"/></svg>

<section class="custom">
  <div class="aqua-band"></div>
  <div class="certified">Certified by<br>Marbrook Jeweler.</div>
  <div class="ph" role="img" aria-label="Rose gold diamond engagement ring on display stand" style="left:314px;top:728px;width:290px;height:282px;background:radial-gradient(circle at 50% 45%,#d8b7a5,#6b5146 55%,#3b2c26)"></div>
  <a class="btn-outline" style="left:470px;top:968px;width:118px;height:28px;border-width:1px;background:#fff">See Our Designs</a>
  <h2>Custom<br>Jewelery Services.</h2>
  <p>We like to say, “If you can dream it, we can make it!” If you’ve seen a ring or other piece of jewelry you like, we can recreate it. If you’ve designed a piece yourself, we can create it. We are your custom design specialists!</p>
  <a class="text-link" style="left:651px;top:958px">More about Custom Jewelery Services</a>
</section>

<section class="split">
  <div class="ph" role="img" aria-label="Jeweler's hands polishing a ring with a rotary tool" style="left:190px;top:1090px;width:414px;height:462px;background:linear-gradient(160deg,#7a5a46,#3a2a22 55%,#1e1713)"></div>
  <div class="ph" style="left:604px;top:1090px;width:414px;height:462px;background:#e8e9eb"></div>
  <div class="ph" role="img" aria-label="Portrait of woman wearing jewelry" style="left:775px;top:1090px;width:243px;height:462px;background:linear-gradient(180deg,#5a4032,#2a1f1a 70%,#1a1a1a)"></div>
  <div class="split-label">Jewelry Repair Services</div>
  <div class="split-title">Good as new &amp;<br>Customized for you.</div>
  <div class="res-title">Our<br>resources</div>
  <a class="text-link" style="left:648px;top:1326px">Marbrook Jewelers Resources</a>
</section>

<section class="features">
  <h2>Features Items</h2>
  <div class="card" style="left:242px;top:1670px"><div class="pic" role="img" aria-label="Solitaire ring with red stone" style="background:radial-gradient(circle,#e6e6e6,#fff 70%)"></div><div class="name">Solitaire Ring</div><div class="price">$165.00–$1,392.00</div></div>
  <div class="card" style="left:485px;top:1670px"><div class="pic" role="img" aria-label="Two-tone wristwatch" style="background:radial-gradient(circle,#d8cdb4,#fff 70%)"></div><div class="name">Claddagh Ring</div><div class="price">$559.00</div></div>
  <div class="card" style="left:728px;top:1670px"><div class="pic" role="img" aria-label="Diamond line bracelet" style="background:radial-gradient(circle,#ebe2df,#fff 70%)"></div><div class="name">Diamond Line Bracelet</div><div class="price">$3,231.00–$3,579.00</div></div>
  <div class="card" style="left:242px;top:1972px"><div class="pic" role="img" aria-label="Dark pearl dome ring" style="background:radial-gradient(circle,#9aa3a8,#fff 70%)"></div><div class="name">Evil Eye Dome Ring</div><div class="price">$92.00–$1,495.00</div></div>
  <div class="card" style="left:485px;top:1972px"><div class="pic" role="img" aria-label="Accented engagement ring" style="background:radial-gradient(circle,#e0e0e0,#fff 70%)"></div><div class="name">Accented Engagement Ring</div><div class="price">$198.00–$1,928.00</div></div>
  <div class="card" style="left:728px;top:1972px"><div class="pic" role="img" aria-label="Ring with blue accent stone" style="background:radial-gradient(circle,#dfe7ea,#fff 70%)"></div><div class="name">Accented Ring</div><div class="price">$165.00–$1,370.00</div></div>
  <div class="browse">Browse our online collection of fine jewelry and then visit us in person.<br>Together we’ll find a piece that speaks from the heart.</div>
  <div class="browse-rule"></div>
</section>

<section class="heritage">
  <div class="ph" role="img" aria-label="Dark foliage backdrop with rings" style="left:720px;top:90px;width:480px;height:360px;background:radial-gradient(ellipse at 50% 50%,#5d4a3a,#2a2620 50%,rgba(18,23,34,0) 75%)"></div>
  <h2>Jewelry crafted<br>with decades of experience<br>since <b>1990.</b></h2>
  <div class="vrule"></div>
  <p>From “will you?” to “I do” and every momentous occasion in between, Marbrook Jewelers offers a radiant array of elegant stones and settings to take her breath away. Our family-owned store here in Ashford, MN upholds this promise we made more than 40 years ago: to provide professional expertise that helps you give a gift with a personal touch.</p>
  <a class="text-link">Read more about us</a>
</section>

<section class="showcase">
  <div class="ph" role="img" aria-label="Necklace on black bust with colored gemstones" style="left:160px;top:55px;width:240px;height:290px;background:radial-gradient(circle at 50% 45%,#3a3a3a,#5a5a5a 40%,rgba(231,231,231,0) 70%)"></div>
  <div class="ph" role="img" aria-label="Hand wearing a diamond ring" style="left:760px;top:15px;width:200px;height:490px;background:linear-gradient(180deg,#f0d9cb,#e6c3b0)"></div>
</section>
<div class="partner-mark">Tandem &amp; Vow</div>
<h2 class="showcase-title serif">Marbrook Showcase</h2>
<div class="showcase-text">Flexible designs enabling you to personalize jewelry to match your story and personality</div>
<a class="btn-outline btn-shadow" style="left:537px;top:3248px;width:123px;height:28px;border-width:1.5px">View details</a>

<section class="engrave">
  <div class="engrave-band"></div>
  <div class="ph" role="img" aria-label="Green leaves decoration" style="left:0;top:3460px;width:100px;height:180px;border-radius:10% 50% 10% 50%;background:linear-gradient(135deg,#9fbf7c,#5f8a49)"></div>
  <div class="ph" role="img" aria-label="Engraved heartbeat bar necklace on display" style="left:153px;top:3365px;width:385px;height:555px;background:linear-gradient(180deg,#c79a55,#e8e6e2 35%,#dcd9d4)"></div>
  <div class="ph" role="img" aria-label="Glass and crystal trophies and awards" style="left:548px;top:3410px;width:497px;height:380px;background:linear-gradient(135deg,#27344a,#1c2536)"></div>
  <div class="engrave-card">Engraving &amp;<br>Trophies</div>
  <a class="btn-small" style="left:583px;top:3823px;width:120px">Engraving photos</a>
  <a class="btn-small" style="left:583px;top:3863px;width:170px">Browse catalogs collections</a>
</section>

<section class="gallery">
  <div class="ph" role="img" aria-label="Couple outdoors in autumn" style="left:190px;top:4080px;width:195px;height:182px;background:linear-gradient(180deg,#a58a4e,#6d6a55)"></div>
  <div class="ph" role="img" aria-label="Family portrait outdoors" style="left:397px;top:4080px;width:195px;height:182px;background:linear-gradient(180deg,#c9b07a,#8a7d62)"></div>
  <div class="ph" role="img" aria-label="Store interior with display cases" style="left:603px;top:4080px;width:195px;height:182px;background:linear-gradient(180deg,#8a6a3e,#d3a85e)"></div>
  <div class="ph" role="img" aria-label="Storefront exterior" style="left:810px;top:4080px;width:195px;height:182px;background:linear-gradient(180deg,#4e5366,#2a2d38)"></div>
  <div class="gallery-card"><h3>Our Gallery</h3><span>View all our gallery</span></div>
</section>

<section class="gifts">
  <div class="ph" role="img" aria-label="Gold heart locket pendant" style="left:0;top:-10px;width:130px;height:230px;background:radial-gradient(circle at 45% 60%,#c9a24a,#b08a3a 40%,rgba(233,233,233,0) 70%)"></div>
  <div class="ph" role="img" aria-label="Gift box with money clip" style="left:360px;top:-80px;width:280px;height:430px;background:linear-gradient(160deg,#f4f4f4,#dcdcdc)"></div>
  <div class="ph" role="img" aria-label="White paper flowers decoration" style="left:1060px;top:30px;width:140px;height:370px;background:linear-gradient(180deg,#f2ede6,#e2dbd0)"></div>
</section>
<h2 class="gift-title serif">Surprise your loved<br>one with beautiful<br>gift items</h2>
<a class="btn-gold">View gift ideas</a>
<div class="pen-card"><div class="ph" role="img" aria-label="Engraved pen" style="left:25px;top:30px;width:123px;height:165px;background:radial-gradient(circle,#c9b8b8,#fff 70%)"></div></div>

<footer class="site-footer">
  <div class="ph" role="img" aria-label="Emerald and diamond pendant" style="left:60px;top:30px;width:230px;height:150px;background:radial-gradient(circle at 45% 55%,#2d8a5e,#5a5a5a 40%,rgba(29,29,29,0) 70%)"></div>
  <div class="f-info">Marbrook Jewelers<br>48 Linden Ave N, Ashford, MN<br>555-214-7730 - Phone<br>888-555-0192 - Toll Free</div>
  <a class="f-btn">View our store location</a>
  <div class="f-rule" style="left:575px"></div>
  <div class="ph" style="left:604px;top:60px;width:46px;height:46px;border-radius:50%;background:#e6e6e6"></div>
  <div class="ph" style="left:665px;top:62px;width:58px;height:40px;background:#e6e6e6"></div>
  <div class="ph" style="left:612px;top:145px;width:125px;height:38px;background:#e6e6e6"></div>
  <div class="f-rule" style="left:792px"></div>
  <div class="social" style="top:84px"><i></i>Snapgrid</div>
  <div class="social" style="top:130px"><i></i>Friendwall</div>
  <div class="copyright">©2022 Marbrook Jewelers: Minnesota Jeweler. All Rights Reserved.</div>
</footer>

</body>
</html>
```